MS Word and MS Powerpoint template creation using existing logo as style guide

Create a professional looking MS Word document template and MS powerpoint template for Korvath Advisory Pty Ltd using a logo that's already been created as the style guide. Korvath is a professional services business providing strategy, governance and execution support to small and medium business, Boards and executive teams. refer design brief.

Target Market(s)

Small to medium business, Chairs, Boards, executive teams, general managers

Industry/Entity Type

Professional business services, consultancy, business support outsourcing

Font styles to use
Other font styles liked:
• calibri

Requirements
Must have
• leverage the existing logo for colour scheme. Use the KORVATH logo type font. Fully editable templates Word and MS Powerpoint,
Nice to have
• Refer to the design brief
Should not have
• animations, cartoons, stock images of people.

```html
<!DOCTYPE html>
<html lang="en">
<head>
<meta charset="utf-8">
<title>Korvath Advisory – Board Presentation, Letter and Report Templates</title>
<link rel="stylesheet" href="https://fonts.googleapis.com/css2?family=Carlito:wght@400;700&family=Montserrat:wght@500&display=swap">
<style>
  :root {
    --navy: #1f3650;
    --navy-deep: #18293d;
    --slide-top: #22384f;
    --slide-bottom: #16263a;
    --ink: #2a2f36;
    --ink-soft: #5a6069;
    --rule: #c9ced5;
    --paper: #ffffff;
    --backdrop: #eef0f2;
    --on-dark: #f2f4f7;
  }
  * { box-sizing: border-box; margin: 0; padding: 0; }
  html, body { width: 1200px; height: 699px; overflow: hidden; }
  body {
    background: var(--backdrop);
    font-family: "Carlito", "Calibri", sans-serif;
    color: var(--ink);
    position: relative;
  }
  .wordmark {
    font-family: "Montserrat", sans-serif;
    font-weight: 500;
    letter-spacing: 0.22em;
    color: var(--navy);
  }

  /* Presentation title slide */
  .title-slide {
    position: absolute;
    left: 340px; top: 34px;
    width: 520px; height: 293px;
    background: linear-gradient(160deg, var(--slide-top), var(--slide-bottom));
    color: var(--on-dark);
    text-align: center;
    box-shadow: 0 6px 18px rgba(20, 30, 45, 0.18);
  }
  .title-slide .wordmark {
    color: var(--on-dark);
    font-size: 36px;
    margin-top: 88px;
    padding-left: 0.22em;
  }
  .title-slide .entity {
    font-size: 11px;
    letter-spacing: 0.06em;
    margin-top: 4px;
  }
  .title-slide .deck-title {
    font-size: 24px;
    letter-spacing: 0.02em;
    margin-top: 22px;
  }
  .title-slide .tagline {
    font-size: 12.5px;
    letter-spacing: 0.03em;
    margin-top: 4px;
  }

  /* Shared page styles */
  .page {
    position: absolute;
    top: 348px;
    height: 340px;
    background: var(--paper);
    box-shadow: 0 4px 16px rgba(20, 30, 45, 0.14);
    overflow: hidden;
  }
  .page-head { text-align: center; padding-top: 16px; }
  .page-head .wordmark { font-size: 22px; padding-left: 0.22em; }
  .page-head .tagline {
    font-size: 8.5px;
    letter-spacing: 0.08em;
    text-transform: uppercase;
    color: var(--ink-soft);
    margin-top: 1px;
  }
  .band {
    background: var(--navy);
    color: var(--on-dark);
    font-weight: 700;
    letter-spacing: 0.06em;
    text-transform: uppercase;
  }

  /* Letter template */
  .letter { left: 110px; width: 470px; padding: 0 46px; font-size: 8.5px; line-height: 1.3; }
  .letter .head-rule { height: 2px; background: var(--navy); margin: 7px 0 3px; }
  .letter .band { text-align: center; font-size: 11px; padding: 3px 0; }
  .letter .meta { margin-top: 8px; }
  .letter .meta b { display: block; margin-top: 3px; }
  .letter .address { margin-top: 1px; color: var(--ink-soft); }
  .letter .subject { display: flex; gap: 60px; margin-top: 5px; font-weight: 700; }
  .letter .salutation { margin-top: 6px; }
  .letter p { margin-top: 5px; }
  .letter ul { margin: 4px 0 0 18px; }

  /* Report template */
  .report { left: 640px; width: 450px; padding: 0 34px; font-size: 8.5px; line-height: 1.3; }
  .report .band { font-size: 10px; padding: 2px 8px; margin-top: 6px; }
  .report .band.main { text-align: center; font-size: 12px; padding: 3px 0; margin-top: 7px; }
  .report .row {
    display: flex; justify-content: space-between;
    border-bottom: 1px solid var(--rule);
    padding: 1.5px 8px;
  }
  .report .row span:last-child { color: var(--ink-soft); }
</style>
</head>
<body>

  <section class="title-slide" aria-label="Presentation title slide">
    <div class="wordmark">KORVATH</div>
    <div class="entity">KORVATH ADVISORY PTY LTD</div>
    <div class="deck-title">BOARD PRESENTATION</div>
    <div class="tagline">CONNECTING STRATEGY, GOVERNANCE &amp; EXECUTION</div>
  </section>

  <article class="page letter" aria-label="Letter template">
    <header class="page-head">
      <div class="wordmark">KORVATH</div>
      <div class="tagline">Connecting Strategy, Governance &amp; Execution</div>
    </header>
    <div class="head-rule"></div>
    <div class="band">Korvath Advisory</div>
    <div class="meta">
      <b>Date</b>
      <b>To</b>
      <div class="address">Client Name, Korvath Advisory Pty Ltd<br>Level 2, 18 Sample Street, Sampletown 0000</div>
    </div>
    <div class="subject"><span>Subject</span><span>Connecting Strategy, Governance Subject</span></div>
    <div class="salutation">Dear Management,</div>
    <p>Thank you for the opportunity to support your board. This letter outlines our proposed approach, scope and timing for the engagement ahead.</p>
    <ul>
      <li>This engagement aligns strategy, governance and execution priorities.</li>
      <li>Our team will work closely with your executives each month.</li>
    </ul>
    <p>We offer a focused set of services across our practice areas:</p>
    <ul>
      <li>Strategy Insights</li>
      <li>Operational Review</li>
      <li>Governance Protocols</li>
      <li>Portal Access</li>
    </ul>
    <p>We welcome the chance to discuss how we can add value to your company.</p>
  </article>

  <article class="page report" aria-label="Report template">
    <header class="page-head">
      <div class="wordmark">KORVATH</div>
      <div class="tagline">Connecting Strategy, Governance &amp; Execution</div>
    </header>
    <div class="band main">Report</div>
    <div class="row"><span>Client name</span><span>Korvath Advisory Pty Ltd</span></div>
    <div class="row"><span>Prepared by</span><span>Strategy Team</span></div>
    <div class="row"><span>Document</span><span>Board Paper</span></div>

    <div class="band">Executive Summary</div>
    <div class="row"><span>Purpose and scope</span><span></span></div>
    <div class="row"><span>Key findings</span><span></span></div>
    <div class="row"><span>Recommendations summary</span><span></span></div>

    <div class="band">Performance Review</div>
    <div class="row"><span>Financial results</span><span></span></div>
    <div class="row"><span>Operational metrics</span><span></span></div>

    <div class="band">Risk &amp; Governance</div>
    <div class="row"><span>Risk register update</span><span></span></div>
    <div class="row"><span>Compliance report</span><span></span></div>

    <div class="band">Strategic Priorities</div>
    <div class="row"><span>Initiatives status</span><span></span></div>
  </article>

</body>
</html>
```